・電子書籍の表紙デザインをお願いします。

・本の内容
モヤモヤグルグルしてるただの主婦でも、天職につながれば稼げるようになる。
自分の事を理解し天職につながることによって、
自信や人間関係やお金、仕事や健康までも、うまく回り始める。
私のエピソードから天職につながるプロセスを見てもらって解説してます。
後半で、あなたの天職につながるワークを実践して
スモールステップを踏み出せるようになるという内容になっています。

・デザイン要望
文字を大きく、パッと見て何が書いてあるかわかりやすいようにして欲しいです。

その他何かありましたら、気軽に質問して下さいね。
よろしくお願いいたします。

タイトルとして

スル~っととんとん拍子に
『ひらめく毎日!をひらく本』
モヤモヤグルグルしてたただの主婦の私が、
まさかの経営者になった理由
森川遥香

読者限定プレゼント
「何かしたい」でも「何をしたいのかわからない」
そんなあなたに
「星読みカルテ」プレゼント

入れて欲しいです。
とんとん拍子 → トントン拍子

軽快なイメージに一番近かったです。

皆さんのご提案、すべて素敵で迷いました。
ありがとうございました。

```html
<!DOCTYPE html>
<html lang="ja">
<head>
<meta charset="UTF-8">
<title>ひらめく毎日!をひらく本</title>
<link rel="stylesheet" href="https://fonts.googleapis.com/css2?family=Noto+Sans+JP:wght@500;700;900&display=swap">
<style>
  :root {
    --pink: #e5185d;
    --pink-soft: #fde3ea;
    --ink: #1a1a1a;
    --paper: #ffffff;
  }
  * { margin: 0; padding: 0; box-sizing: border-box; }
  html, body { width: 750px; height: 1200px; overflow: hidden; background: var(--paper); }
  body { font-family: "Noto Sans JP", sans-serif; color: var(--ink); }
  .cover {
    position: relative; width: 750px; height: 1200px;
    background: var(--paper);
    border: 18px solid var(--pink);
  }
  .tagline {
    position: absolute; left: 20px; top: 14px;
    width: 192px; padding: 12px 6px 14px;
    border: 4px solid var(--pink); border-radius: 14px;
    color: var(--pink); font-weight: 700; font-size: 27px; line-height: 1.25;
    text-align: center; background: var(--paper);
  }
  .tagline::after {
    content: ""; position: absolute; right: -18px; top: 42px;
    border-left: 18px solid var(--pink); border-top: 10px solid transparent; border-bottom: 10px solid transparent;
  }
  .title { position: absolute; left: 0; right: 0; top: 8px; text-align: center; font-weight: 900; line-height: 1; }
  .title-line { display: block; }
  .title-line--first { padding-left: 200px; font-size: 120px; letter-spacing: -2px; }
  .title-line--key { margin-top: 8px; font-size: 120px; }
  .title-line--key .accent { color: var(--pink); font-size: 200px; letter-spacing: -6px; }
  .title-line--last { margin-top: 4px; font-size: 126px; letter-spacing: -2px; }
  .subtitle {
    position: absolute; left: 0; right: 0; top: 520px;
    text-align: center; font-weight: 900; font-size: 40px; line-height: 1.45; color: #333;
  }
  .author {
    position: absolute; left: 0; right: 0; top: 728px;
    text-align: center; font-weight: 900; font-size: 40px; color: #333;
  }
  .author small { font-size: 24px; margin-right: 16px; vertical-align: 6px; }
  .gift {
    position: absolute; left: 0; right: 0; bottom: 0; height: 330px;
    background: var(--pink); padding: 18px;
  }
  .gift-panel {
    position: relative; height: 100%; background: var(--pink-soft);
    display: flex; align-items: center; padding: 0 20px;
  }
  .gift-badge {
    flex: none; width: 200px; height: 200px; border-radius: 50%;
    background: var(--paper); border: 6px solid var(--pink);
    display: flex; align-items: center; justify-content: center; text-align: center;
    color: var(--pink); font-weight: 900; font-size: 30px; line-height: 1.3;
  }
  .gift-text {
    margin-left: 22px; color: var(--pink); font-weight: 700; font-size: 23px; line-height: 1.6;
  }
  .gift-text strong { display: block; font-size: 34px; font-weight: 900; margin-top: 4px; }
</style>
</head>
<body>
  <main class="cover">
    <p class="tagline">スル〜っと<br>トントン拍子に</p>
    <h1 class="title">
      <span class="title-line title-line--first">ひらめく</span>
      <span class="title-line title-line--key"><span class="accent">毎日</span>!を</span>
      <span class="title-line title-line--last">ひらく本</span>
    </h1>
    <p class="subtitle">モヤモヤグルグルしてた<br>ただの主婦の私が、<br>まさかの経営者になった理由</p>
    <p class="author"><small>著者</small>森川遥香</p>
    <section class="gift">
      <div class="gift-panel">
        <div class="gift-badge">読者限定<br>プレゼント</div>
        <p class="gift-text">「何かしたい!」でも、<br>「自分が何したいのかがわからない!」<br>そんなあなた自身を活かす<strong>星読みカルテ付き</strong></p>
      </div>
    </section>
  </main>
</body>
</html>
```